Harrowgate Supply Group Business Card Design

The Business Card will be one side only with Harrowgate Supplies Group Logo
Card should have:
Name
Title
Office phone Number
Cell Number
email address
Website
Street Address
Our Slogan is Rugged and Reliable
Looking for something that stands out from other business cards

Target Market(s)

Heavy equipment Lease Company

```html
<!DOCTYPE html>
<html lang="en">
<head>
<meta charset="utf-8">
<title>Harrowgate Supplies Group – Business Card</title>
<link rel="stylesheet" href="https://fonts.googleapis.com/css2?family=Roboto:wght@400;500;700;900&display=swap">
<style>
  :root {
    --backdrop: #3b3b3d;
    --card: #2a2070;
    --card-deep: #231a60;
    --red: #e3262d;
    --white: #ffffff;
    --muted: #8f86c9;
  }
  * { box-sizing: border-box; margin: 0; padding: 0; }
  html, body { width: 799px; height: 1200px; overflow: hidden; }
  body {
    background: var(--backdrop);
    font-family: "Roboto", Arial, sans-serif;
    position: relative;
  }
  .card {
    position: absolute;
    left: 80px;
    width: 640px;
    height: 366px;
    border-radius: 26px;
    background: linear-gradient(160deg, var(--card) 0%, var(--card-deep) 100%);
    overflow: hidden;
  }
  .card--front { top: 117px; }
  .card--back { top: 717px; }

  /* Front */
  .front-brand {
    position: absolute;
    top: 128px; left: 0; right: 0;
    text-align: center;
    color: var(--muted);
    font-weight: 900;
    font-size: 30px;
    letter-spacing: 1px;
    text-transform: uppercase;
  }
  .front-brand .dot {
    display: inline-block;
    width: 22px; height: 22px;
    border-radius: 50%;
    background: var(--muted);
    vertical-align: -2px;
    margin-right: 12px;
  }
  .front-web {
    position: absolute;
    top: 268px; left: 0; right: 0;
    display: flex; align-items: center; justify-content: center; gap: 18px;
    color: var(--white);
    font-size: 17px;
  }
  .rule { width: 60px; height: 3px; background: var(--red); border-radius: 2px; }

  /* Back */
  .back-brand {
    position: absolute;
    top: 104px; left: 34px;
    width: 280px;
    display: flex; align-items: center; gap: 12px;
  }
  .back-brand .dot {
    width: 30px; height: 30px; border-radius: 50%; background: var(--white); flex: none;
  }
  .back-brand .name {
    color: var(--red);
    font-weight: 900;
    font-size: 18px;
    line-height: 1.2;
    text-transform: uppercase;
    letter-spacing: .3px;
  }
  .slogan {
    position: absolute;
    top: 298px; left: 70px;
    display: flex; align-items: center; gap: 12px;
    color: var(--white);
    font-size: 18px;
  }
  .slogan em { font-style: normal; color: var(--red); }
  .slogan .tick { width: 22px; height: 3px; background: var(--red); }

  .contact {
    position: absolute;
    top: 92px; left: 370px;
    color: var(--white);
  }
  .contact-name { color: var(--red); font-weight: 500; font-size: 26px; line-height: 1.1; }
  .contact-title { font-size: 16px; margin-bottom: 12px; }
  .contact-list { list-style: none; font-size: 16px; line-height: 23px; }
  .contact-list li { display: flex; align-items: center; gap: 10px; white-space: nowrap; }
  .contact-list svg { width: 12px; height: 12px; fill: var(--red); flex: none; }
  .contact-list .plain { margin-left: -22px; }
</style>
</head>
<body>

<section class="card card--front" aria-label="Card front">
  <div class="front-brand"><span class="dot"></span>Harrowgate Supplies Group</div>
  <div class="front-web">
    <span class="rule"></span>
    <span>www.harrowgatesupply.com</span>
    <span class="rule"></span>
  </div>
</section>

<section class="card card--back" aria-label="Card back">
  <div class="back-brand">
    <span class="dot"></span>
    <span class="name">Harrowgate Supplies<br>Group</span>
  </div>

  <div class="slogan">
    <span class="tick"></span>
    <span>Rugged <em>and</em> Reliable</span>
    <span class="tick"></span>
  </div>

  <div class="contact">
    <div class="contact-name">Daniel Harlow</div>
    <div class="contact-title">Managing Director</div>
    <ul class="contact-list">
      <li>
        <svg viewBox="0 0 12 12"><path d="M2 1h3l1 3-1.5 1a6 6 0 0 0 2.5 2.5L8 6l3 1v3a1 1 0 0 1-1 1A9 9 0 0 1 1 2a1 1 0 0 1 1-1z"/></svg>
        <span>222-333-4444</span>
      </li>
      <li>
        <svg viewBox="0 0 12 12"><rect x="3.5" y="0.5" width="5" height="11" rx="1"/></svg>
        <span>444-555-6666</span>
      </li>
      <li>
        <svg viewBox="0 0 12 12"><path d="M0 2h12v8H0z M0 2l6 4 6-4" /></svg>
        <span>name@harrowgatesupply.com</span>
      </li>
      <li>
        <svg viewBox="0 0 12 12"><circle cx="6" cy="6" r="5.5"/></svg>
        <span>www.harrowgatesupply.com</span>
      </li>
      <li class="plain"><span>1234 Anywhere, Any City, Country</span></li>
    </ul>
  </div>
</section>

</body>
</html>
```